Ridge Contracting LLC Business Card Design

I am looking for a creative and unique business card design. We are a commercial construction general contractor. With the name "RIDGE" Contracting, I am hoping to see some neat designs that correlate with the name.

```html
<!DOCTYPE html>
<html lang="en">
<head>
<meta charset="utf-8">
<title>Ridge Contracting LLC – Business Card</title>
<link rel="stylesheet" href="https://fonts.googleapis.com/css2?family=Montserrat:wght@500;600;700&display=swap">
<style>
  :root {
    --page-bg: #d9d3ca;
    --card-bg: #ece7df;
    --card-edge: #f6f2ec;
    --brand-blue: #1c6e98;
    --ink: #262626;
    --divider: #2a6f93;
  }
  html, body {
    margin: 0;
    padding: 0;
    width: 1200px;
    height: 1047px;
    overflow: hidden;
    background: var(--page-bg);
    font-family: "Montserrat", sans-serif;
  }
  .card {
    position: absolute;
    left: 120px;
    top: 262px;
    width: 960px;
    height: 524px;
    border-radius: 26px;
    background: var(--card-bg);
    box-shadow: inset 0 0 0 2px var(--card-edge), 0 10px 30px rgba(0,0,0,0.08);
  }
  .brand {
    position: absolute;
    left: 60px;
    top: 205px;
    width: 340px;
    text-align: center;
    color: var(--brand-blue);
    font-weight: 700;
  }
  .brand-name {
    display: block;
    font-size: 64px;
    letter-spacing: 4px;
    line-height: 1;
  }
  .brand-sub {
    display: block;
    font-size: 18px;
    letter-spacing: 7px;
    margin-top: 8px;
  }
  .divider {
    position: absolute;
    left: 474px;
    top: 84px;
    width: 2px;
    height: 354px;
    background: var(--divider);
  }
  .details {
    position: absolute;
    left: 523px;
    top: 108px;
    color: var(--ink);
  }
  .person-name {
    margin: 0;
    font-size: 39px;
    font-weight: 700;
    color: var(--brand-blue);
    line-height: 1.1;
  }
  .person-role {
    margin: 4px 0 0;
    font-size: 21px;
    font-weight: 500;
  }
  .address {
    margin: 26px 0 0;
    font-size: 23px;
    font-weight: 500;
    line-height: 36px;
    font-style: normal;
  }
  .contact-list {
    list-style: none;
    margin: 14px 0 0;
    padding: 0;
    font-size: 23px;
    font-weight: 500;
  }
  .contact-list li {
    display: flex;
    align-items: center;
    height: 37px;
  }
  .contact-icon {
    width: 18px;
    height: 18px;
    margin-right: 13px;
    fill: var(--brand-blue);
  }
</style>
</head>
<body>
  <div class="card">
    <div class="brand" aria-label="Ridge Contracting">
      <span class="brand-name">RIDGE</span>
      <span class="brand-sub">CONTRACTING</span>
    </div>

    <div class="divider"></div>

    <div class="details">
      <h1 class="person-name">Owen Hartley</h1>
      <p class="person-role">Managing Director</p>
      <address class="address">Your address, City<br>State, Zip 1234</address>
      <ul class="contact-list">
        <li>
          <svg class="contact-icon" viewBox="0 0 20 20" aria-hidden="true">
            <path d="M2 7c0-2 3-4 8-4s8 2 8 4v1.5h-4V7c-1-.6-2.5-.9-4-.9S7 6.4 6 7v1.5H2z"/>
            <path d="M5 10h10l2 7H3z"/>
          </svg>
          <span>123 456 789</span>
        </li>
        <li>
          <svg class="contact-icon" viewBox="0 0 20 20" aria-hidden="true">
            <path d="M2 5h16v10H2z"/>
            <path d="M2.5 5.5 10 11l7.5-5.5" fill="none" stroke="#ece7df" stroke-width="1.4"/>
          </svg>
          <span>info@ridgecontracting.com</span>
        </li>
        <li>
          <svg class="contact-icon" viewBox="0 0 20 20" aria-hidden="true">
            <circle cx="10" cy="10" r="8"/>
            <path d="M6 6c2 0 3 1 3 2.5S7 10 7 12s2 2 2 4M12 4.5c-.5 1.5 1 2.5 2.5 2.5M13 11c1 0 2 1 1.5 3" fill="none" stroke="#ece7df" stroke-width="1.4"/>
          </svg>
          <span>www.ridgecontracting.com</span>
        </li>
      </ul>
    </div>
  </div>
</body>
</html>
```